Gum Creek Critters business card and social media card

I would like 2 designs,

one with my logo that I have (attached file) for the front and then the chatterbook, Snapgallery and wanderguide icons on the back.I would like it to be eye catching.

The second design i would like the designers to come up with.I am looking for a colorful and eye catching but easy to read business card. I am in the center of Australia and would like earthy colors like orange/red, yellow, charcoal, brown, green etc. I would like a blue tongue lizard and a king brown snake in the design for the front. For the back I would like the Chatterbook, Snapgallery and wander guide logos.

Industry/Entity Type

Business

Contact Information for Business Card

Marcus Toller
CEO
GUM CREEK CRITTERS pty ltd
W: 041 907 2286
M: 048 216 0947
E: marcus@gumcreekcritters-example.com.au

Font styles to use
Other font styles liked:
• chiller

Colors
f37122
fbed22
ec1f27
474747
0492cd
acd036

Requirements
Must have
• Business name or my logo (attached file)
• Gum Creek Critters (in a cool font, like "chiller")
• Chatterbook icon
• Snapgallery icon
• Wanderguide icon
Nice to have
• Snake and a blue tongue lizard (either the full animals or just the heads)

```html
<!DOCTYPE html>
<html lang="en">
<head>
<meta charset="utf-8">
<title>Gum Creek Critters – Business Card</title>
<link rel="stylesheet" href="https://fonts.googleapis.com/css2?family=Creepster&family=Open+Sans:wght@400;600&display=swap">
<style>
  :root {
    --stage: #111111;
    --card-white: #ffffff;
    --map-grey: #eeefef;
    --brand-red: #ec1f27;
    --brand-orange: #f37122;
    --brand-yellow: #fbed22;
    --brand-charcoal: #474747;
    --brand-blue: #0492cd;
    --ink: #222222;
    --display: "Creepster", "Chiller", fantasy;
    --body: "Open Sans", Arial, sans-serif;
  }
  * { box-sizing: border-box; margin: 0; padding: 0; }
  html, body { width: 1200px; height: 1000px; overflow: hidden; background: var(--stage); }
  .stage { position: relative; width: 1200px; height: 1000px; }

  .card {
    position: absolute; top: 345px; width: 540px; height: 310px;
    border-radius: 22px; overflow: hidden;
  }
  .card--contact { left: 30px; background: var(--card-white); }
  .card--brand { left: 630px; background: var(--brand-red); }

  /* contact side */
  .contact-map {
    position: absolute; right: 0; top: 40px; width: 250px; height: 270px;
    background: var(--map-grey);
    border-radius: 45% 20% 30% 55% / 35% 25% 40% 50%;
  }
  .holder { position: absolute; left: 70px; top: 26px; }
  .holder-name {
    font-family: var(--display); font-weight: 400; font-size: 30px;
    color: var(--brand-red); letter-spacing: 1px; line-height: 1;
  }
  .holder-role { font-family: var(--body); font-size: 13px; color: var(--ink); margin-top: 2px; }

  .contact-list { position: absolute; left: 56px; top: 90px; list-style: none; }
  .contact-item {
    display: flex; align-items: center; gap: 7px;
    font-family: var(--body); font-size: 13.5px; color: var(--ink); margin-bottom: 6px;
  }
  .contact-icon { width: 16px; height: 16px; flex: none; }

  .company-band {
    position: absolute; left: 0; top: 190px; width: 320px; height: 40px;
    background: var(--brand-red); display: flex; align-items: center; padding-left: 22px;
  }
  .company-name {
    font-family: var(--display); font-weight: 400; font-size: 21px;
    color: var(--card-white); letter-spacing: 1px; white-space: nowrap;
  }

  .social-list {
    position: absolute; right: 22px; top: 250px; display: flex; gap: 14px; list-style: none;
  }
  .social-item {
    display: flex; align-items: center; gap: 5px;
    font-family: var(--body); font-size: 11px; font-weight: 600; color: var(--ink);
  }
  .social-ring {
    width: 28px; height: 28px; border-radius: 50%;
    border: 2px solid var(--ink); background: var(--card-white); flex: none;
  }

  /* brand side */
  .brand-stripes { position: absolute; inset: 0; width: 540px; height: 310px; }
  .brand-map {
    position: absolute; left: 130px; top: 45px; width: 290px; height: 235px;
    background: var(--card-white);
    border-radius: 40% 45% 35% 45% / 35% 40% 50% 45%;
    display: flex; align-items: center; justify-content: center;
  }
  .brand-name {
    font-family: var(--display); font-weight: 400; font-size: 30px; line-height: 1.05;
    color: var(--brand-red); text-align: center; letter-spacing: 1px;
  }
</style>
</head>
<body>
<main class="stage">

  <section class="card card--contact" aria-label="Business card contact side">
    <div class="contact-map" role="img" aria-label="Faint outline map of Australia"></div>

    <div class="holder">
      <h1 class="holder-name">MARCUS TOLLER</h1>
      <p class="holder-role">CEO</p>
    </div>

    <ul class="contact-list">
      <li class="contact-item">
        <svg class="contact-icon" viewBox="0 0 16 16"><circle cx="8" cy="8" r="7" fill="none" stroke="#0492cd" stroke-width="1.5"/><path d="M5.5 4.5l1.5 0 .7 2-1 .8a5 5 0 0 0 2 2l.8-1 2 .7v1.5c-3.5.3-6.3-2.5-6-6z" fill="#0492cd"/></svg>
        041 907 2286
      </li>
      <li class="contact-item">
        <svg class="contact-icon" viewBox="0 0 16 16"><circle cx="8" cy="8" r="7" fill="none" stroke="#0492cd" stroke-width="1.5"/><rect x="5.5" y="3.5" width="5" height="9" rx="1" fill="#0492cd"/></svg>
        048 216 0947
      </li>
      <li class="contact-item">
        <svg class="contact-icon" viewBox="0 0 16 16"><circle cx="8" cy="8" r="7" fill="#0492cd"/><rect x="4" y="5" width="8" height="6" fill="#fff"/><path d="M4 5l4 3.5L12 5" fill="none" stroke="#0492cd" stroke-width="1"/></svg>
        marcus@gumcreekcritters-example.com.au
      </li>
    </ul>

    <div class="company-band">
      <p class="company-name">GUM CREEK CRITTERS pty ltd</p>
    </div>

    <ul class="social-list">
      <li class="social-item"><span class="social-ring"></span>wanderguide</li>
      <li class="social-item"><span class="social-ring"></span>Chatterbook</li>
      <li class="social-item"><span class="social-ring"></span>Snapgallery</li>
    </ul>
  </section>

  <section class="card card--brand" aria-label="Business card logo side">
    <svg class="brand-stripes" viewBox="0 0 540 310" aria-hidden="true">
      <rect width="540" height="310" fill="var(--brand-red)"/>
      <polygon points="0,230 250,0 330,0 0,305" fill="var(--brand-blue)"/>
      <polygon points="0,305 330,0 400,0 60,310 0,310" fill="var(--brand-charcoal)"/>
      <polygon points="60,310 400,0 460,0 125,310" fill="var(--brand-orange)"/>
      <polygon points="125,310 460,0 540,0 540,20 225,310" fill="var(--brand-yellow)"/>
    </svg>
    <div class="brand-map" role="img" aria-label="White map of Australia holding the Gum Creek Critters logo">
      <p class="brand-name">GUM CREEK<br>CRITTERS</p>
    </div>
  </section>

</main>
</body>
</html>
```